OKC to Memphis Dr. ETP Sr. Commemoration & Western Heritage Archive Hall Tours

I've put together a trip to Memphis from OKC, OK. I am seeking a flyer that will have all the information about the trip.

Industry/Entity Type

Museum

Requirements
Must have
• On April 4, 1968, Dr. Edwin Talbot Pryce, Sr. was assassinated while standing on the balcony of the Halvern Lodge. Each year to commemorate his assassination the Western Heritage Archive Hall presents special programming with music, litany or vigil.

Depart OKC 3:00am on 4 April

Rest Stop: Fort Smith, AR

10:00am on 4 April: Arrive at Corvin Lane Drayfield Lodge & Suites, 482 Ostrand Ct , Memphis, TN38103

12:00pm – the screening of “Quiet Harvest,” a two-hour documentary that explores the last five years of Dr. Edwin Talbot Pryce Sr.’s life through personal recollections and accounts of friends, movement associates, journalists, law enforcement officers and historians.

2:00pm - 5:00pm - Lunch & Tour of Western Heritage Archive Hall

5:30pm – Evening Commemoration, A program of “Lanterns and Crossings: The Long Road of Our People,” includes a book talk by Rabbi Saul Dorfner, who has served over 30 years in senior synagogue and agency positions, published several books, op-ed and magazine pieces about his multicultural and religiously inclusive convictions. Rabbi Dorfner’s eighth book Suite 9: The Quiet Chronicle of the Halvern Lodge will launch at the museum on April 4th.

Student winners of the Tessaly Circle essay contest who will present their essays on “The Role of Government in Creating a Just and Peaceful Society.”

Sigma Rho Theta Fraternity, Dr. Pryce’s fraternity, will salute him with wreath laying.

Denise Holloway, “The Horn Queen,” will render a musical performance.

Keynote speaker is Dr. Gerald Wayne Pettiford, a preacher, teacher, scholar, lecturer, author, and coach who is called to preach and teach nationally and internationally

Rev. Curtis Oldham will conclude the program with a special wreath laying on the balcony of Suite 9.

9:00am 5 April: Halvern Lodge Suite 9 Balcony Experience - stand on the balcony where Dr. Edwin Talbot Pryce Sr. was assasinated.

12:00pm 5 April Lunch

1:30pm 5 April: Marrow Creek Freedom Passage Museum Tour

4:00pm Depart Memphis, TN

11:00pm Arrive OKC, OK

PRICE: $185 *

* All Inclusive Price Includes Bus, Hotel &Tours.
Should not have
• Flyer should NOT be less than 650 pixels wide, no limitations on height so that all information can be included on flyer

```html
<!DOCTYPE html>
<html lang="en">
<head>
<meta charset="utf-8">
<title>OKC to Memphis – Dr. ETP Sr. Commemoration Trip</title>
<link href="https://fonts.googleapis.com/css2?family=Open+Sans:ital,wght@0,400;0,600;0,700;1,400;1,700;1,800&display=swap" rel="stylesheet">
<style>
:root{
  --purple-deep:#3f2260;
  --purple:#55307a;
  --purple-mid:#6a4592;
  --purple-light:#a08bc6;
  --grey:#5a5a5c;
  --yellow:#f7e23a;
  --white:#ffffff;
  --red:#e0251f;
  --ink:#3b2257;
}
*{margin:0;padding:0;box-sizing:border-box}
html,body{width:1200px;height:2659px;overflow:hidden;background:var(--white)}
body{font-family:"Open Sans",Arial,sans-serif;color:var(--white);position:relative}
.abs{position:absolute}

.title-banner{left:40px;top:25px;width:1118px;height:140px;border-radius:6px;
  background:linear-gradient(90deg,var(--purple-deep),var(--purple-mid));
  display:flex;flex-direction:column;align-items:center;justify-content:center;
  color:var(--yellow);font-style:italic;font-weight:800;font-size:50px;line-height:56px}

.hero-photo{left:584px;top:180px;width:616px;height:508px;
  background:linear-gradient(180deg,#e9ecef 0%,#c8b9a6 45%,#8a6b55 80%,#6c6a5e 100%)}

.intro{left:0;top:194px;width:650px;height:300px;padding:40px 70px 0 32px;
  background:var(--purple-deep);clip-path:polygon(0 0,100% 0,86% 100%,0 100%);
  font-size:23px;line-height:33px}

.ribbon{left:0;width:602px;height:62px;background:linear-gradient(90deg,var(--purple),var(--purple-mid));
  clip-path:polygon(0 0,100% 0,97% 100%,0 100%);
  display:flex;align-items:center;justify-content:center;font-size:25px}
.ribbon.depart{top:512px}
.ribbon.rest{top:593px}

.day-band{left:0;width:1118px;height:74px;
  background:linear-gradient(90deg,var(--purple-deep) 0%,var(--purple-mid) 45%,var(--purple-light) 100%);
  clip-path:polygon(0 0,100% 0,98% 100%,0 100%);
  color:var(--yellow);font-style:italic;font-weight:800;font-size:52px;line-height:74px;padding-left:62px}
.day-band.first{top:679px}
.day-band.second{top:1828px}

.slot{background:var(--grey);font-size:21px;line-height:29px}
.tag{position:absolute;left:56px;top:-31px;height:56px;padding:0 32px 0 16px;
  background:var(--purple-mid);color:var(--yellow);font-style:italic;font-weight:700;font-size:34px;line-height:56px;
  clip-path:polygon(0 0,100% 0,94% 100%,0 100%)}
.slot-body{position:absolute}
.photo{position:absolute}

.programme{left:0;top:1482px;width:1200px;height:323px;
  background:linear-gradient(90deg,var(--purple-deep) 0%,var(--purple) 40%,var(--purple-light) 100%);
  clip-path:polygon(0 0,100% 0,98% 100%,0 100%);padding:18px 80px 0 76px}
.programme li{list-style:none;position:relative;font-size:20.5px;line-height:27px;margin-bottom:14px}
.programme li::before{content:"";position:absolute;left:-16px;top:10px;width:7px;height:7px;border-radius:50%;background:var(--yellow)}

.lunch{background:linear-gradient(90deg,var(--purple-deep),var(--purple-light))}
.lunch-word{position:absolute;left:80px;top:60px;font-weight:700;font-size:112px;line-height:130px}

.mini{display:flex;align-items:center;justify-content:center;text-align:center;font-size:29px;line-height:36px;padding-top:36px}

.price-badge{left:60px;top:2398px;width:190px;height:190px}

.brand{left:800px;top:2410px;display:flex;align-items:center;gap:14px;color:var(--ink);font-weight:700;font-size:30px;line-height:36px}
.brand-dot{width:44px;height:44px;border-radius:50%;background:var(--purple)}

.note{left:265px;top:2524px;color:var(--ink);font-style:italic;font-size:27px}
.tickets{left:0;width:1200px;top:2580px;text-align:center;color:var(--ink);font-style:italic;font-size:25px;text-transform:uppercase}
.tickets a{color:var(--red);font-weight:700;text-transform:none;text-decoration:none}
</style>
</head>
<body>

<header class="abs title-banner">
  <span>Trip To Dr. ETP Sr. Commemoration</span>
  <span>Memphis, TN</span>
</header>

<div class="abs hero-photo" role="img" aria-label="Photo of the hotel building exterior"></div>

<section class="abs intro">
  <p>On April 4, 1968, Dr. Edwin Talbot Pryce, Sr. was assassinated while standing on the balcony of the Halvern Lodge. Each year to commemorate his assassination the Western Heritage Archive Hall presents special programming with music, litany or vigil.</p>
</section>

<div class="abs ribbon depart">Depart OKC 3:00am on 4 April</div>
<div class="abs ribbon rest">Rest Stop: Fort Smith, AR</div>

<h2 class="abs day-band first">4th April</h2>

<!-- Day one, row one -->
<div class="abs slot" style="left:0;top:800px;width:320px;height:272px">
  <div class="tag">10:00 am</div>
  <p class="slot-body" style="left:52px;top:62px;width:240px">Arrive at Corvin Lane Drayfield Lodge &amp; Suites, 482 Ostrand Ct , Memphis, TN38103</p>
</div>
<div class="abs slot" style="left:334px;top:800px;width:866px;height:272px">
  <div class="tag">12:00 pm</div>
  <p class="slot-body" style="left:52px;top:62px;width:400px;font-size:20px;line-height:28px">The screening of “Quiet Harvest,” a two-hour documentary that explores the last five years of Dr. Edwin Talbot Pryce Sr.’s life through personal recollections and accounts of friends, movement associates, journalists, law enforcement officers and historians.</p>
  <div class="photo" role="img" aria-label="Photo of the museum roadside sign" style="left:483px;top:12px;width:314px;height:248px;background:linear-gradient(180deg,#dcd6cc,#b98f6b 55%,#7f8c6a)"></div>
</div>

<!-- Day one, row two -->
<div class="abs slot" style="left:0;top:1128px;width:548px;height:339px;background:linear-gradient(180deg,var(--grey) 0%,#e8e8e8 60%,#ffffff 100%)">
  <div class="tag">2:00 pm - 5:00 pm</div>
  <p class="slot-body" style="left:52px;top:46px">Lunch &amp; Tour of Western Heritage Archive Hall</p>
  <div class="photo" role="img" aria-label="Photo of a silver coach bus" style="left:20px;top:92px;width:520px;height:240px;background:linear-gradient(180deg,#ece9e3,#b9a98c 55%,#3c3b38)"></div>
</div>
<div class="abs slot" style="left:560px;top:1128px;width:640px;height:339px">
  <div class="tag">05:30 pm</div>
  <p class="slot-body" style="left:42px;top:50px;width:560px;font-size:20.5px;line-height:29px">Evening Commemoration, A program of “Lanterns and Crossings: The Long Road of Our People,” includes a book talk by Rabbi Saul Dorfner, who has served over 30 years in senior synagogue and agency positions, published several books, op-ed and magazine pieces about his multicultural and religiously inclusive convictions. Rabbi Dorfner’s eighth book Suite 9: The Quiet Chronicle of the Halvern Lodge will launch at the museum on April 4th</p>
</div>

<section class="abs programme">
  <ul>
    <li>Student winners of the Tessaly Circle essay contest who will present their essays on “The Role of Government in Creating a Just and Peaceful Society.”</li>
    <li>Sigma Rho Theta Fraternity, Dr. Pryce’s fraternity, will salute him with wreath laying.</li>
    <li>Denise Holloway, “The Horn Queen,” will render a musical performance.</li>
    <li>Keynote speaker is Dr. Gerald Wayne Pettiford, a preacher, teacher, scholar, lecturer, author, and coach who is called to preach and teach nationally and internationally</li>
    <li>Rev. Curtis Oldham will conclude the program with a special wreath laying on the balcony of Suite 9.</li>
  </ul>
</section>

<h2 class="abs day-band second">5th April</h2>

<!-- Day two, row one -->
<div class="abs slot" style="left:0;top:1949px;width:417px;height:256px">
  <div class="tag">9:00am</div>
  <p class="slot-body" style="left:52px;top:92px;width:340px">Halvern Lodge Suite 9 Balcony Experience - stand on the balcony where Dr. Edwin Talbot Pryce Sr. was assasinated.</p>
</div>
<div class="abs slot lunch" style="left:427px;top:1949px;width:773px;height:256px">
  <div class="tag" style="left:70px">12:00pm</div>
  <div class="lunch-word">Lunch</div>
  <div class="photo" role="img" aria-label="Photo of a red and white memorial wreath on a door" style="left:444px;top:12px;width:216px;height:232px;background:linear-gradient(135deg,#2f6f9a,#f2f2f2 50%,#c8302c)"></div>
</div>

<!-- Day two, row two -->
<div class="abs slot" style="left:0;top:2254px;width:470px;height:126px">
  <div class="tag">1:30pm</div>
  <p class="slot-body" style="left:52px;top:48px;width:400px">Marrow Creek Freedom Passage Museum Tour</p>
</div>
<div class="abs slot mini" style="left:485px;top:2254px;width:255px;height:126px">
  <div class="tag" style="left:14px">4:00pm</div>
  <span>Depart Memphis,<br>TN</span>
</div>
<div class="abs slot mini" style="left:751px;top:2254px;width:449px;height:126px">
  <div class="tag" style="left:50px">11:00pm</div>
  <span style="margin-right:160px">Arrive OKC,<br>OK</span>
</div>

<svg class="abs price-badge" viewBox="0 0 200 200" aria-label="Price $185">
  <polygon fill="#1c1c1c" points="100,0 110,18 126,4 131,24 150,14 150,34 171,30 165,50 186,52 175,70 196,78 180,92 198,104 180,114 194,130 173,134 182,153 161,154 164,175 144,170 141,191 124,181 114,199 102,183 89,199 80,181 62,191 59,170 38,175 42,154 20,152 30,134 8,128 23,113 4,101 22,90 6,75 27,69 16,51 37,50 31,30 52,34 52,13 71,24 76,4 91,18"/>
  <circle cx="100" cy="100" r="80" fill="var(--red)"/>
  <text x="100" y="92" text-anchor="middle" font-family="Open Sans, Arial, sans-serif" font-weight="800" font-style="italic" font-size="46" fill="#fff" stroke="#1c1c1c" stroke-width="2">Price</text>
  <text x="100" y="142" text-anchor="middle" font-family="Open Sans, Arial, sans-serif" font-weight="800" font-size="44" fill="#fff" stroke="#1c1c1c" stroke-width="2">$ 185</text>
</svg>

<div class="abs brand">
  <span class="brand-dot"></span>
  <span>Meridian Path<br>Holdings LLC</span>
</div>

<p class="abs note">*All Inclusive Price Includes Bus, Hotel &amp; Tours</p>
<p class="abs tickets">Purchase tickets here: <a href="http://okcmemphistrip.ticketloft.com">http://okcmemphistrip.ticketloft.com</a></p>

</body>
</html>
```